I am a company selling interior designing materials

HI, I am selling interior design materials and require a namecard which is more outstanding while following a certain details placement as attached.

My clients are mainly interior designers so it has to attract their attention rather than feeling that its "just another namecard". I am selling wallcoverings, fabrics, acoustics and carpets.

Target Market(s)

interior designers designing hotels, commerical offices.

Contact Information for Business Card

As per attached.
Please change address to 47 Jalan 16 Tampines #05-02 Velmora Building Singapore 527314

Font styles to use
Other font styles liked:
• calibri

Requirements
Must have
• (1) company logo on top in the middle. Placement of contac details to be the same
• (2) company color is blue/green cymk 75/8/42/0
• (3) "KTV" logo to be prominent
• (4) You may change the logo but there should be a "swirl" surrounding the word KTV like current logo. The swirl pattern does not need to follow current logo and you may propose.
Should not have
• (1) there should not be any designs above "KTV" logo
• (2) no sharp triangles or angles

```html
<!DOCTYPE html>
<html lang="en">
<head>
<meta charset="utf-8">
<title>KTV Business Card</title>
<link rel="stylesheet" href="https://fonts.googleapis.com/css2?family=Noto+Sans:wght@400;700&display=swap">
<style>
  :root {
    --teal: #4aa593;
    --charcoal: #6b625d;
    --paper: #ffffff;
    --edge: #cfcfcf;
    --blue-1: #0070b0;
    --blue-2: #1483c0;
    --blue-3: #3a92c8;
    --blue-4: #56a9d8;
    --white-text: #ffffff;
  }
  * { box-sizing: border-box; margin: 0; padding: 0; }
  html, body {
    width: 957px; height: 1200px; overflow: hidden;
    background: var(--paper);
    font-family: "Noto Sans", Tahoma, sans-serif;
  }
  .canvas { position: relative; width: 957px; height: 1200px; }
  .card {
    position: absolute; left: 12px; width: 931px;
    background: var(--paper); border: 1px solid var(--edge); overflow: hidden;
  }
  .card--front { top: 14px; height: 562px; }
  .card--back { top: 623px; height: 561px; }

  .wordmark {
    position: absolute; left: 0; right: 0; text-align: center;
    font-weight: 700; color: var(--charcoal); letter-spacing: 2px; line-height: 1;
  }
  .card--front .wordmark { top: 116px; font-size: 100px; }
  .card--back .wordmark { top: 64px; font-size: 66px; }

  .band { position: absolute; left: 0; right: 0; }
  .band--grey { background: var(--charcoal); }
  .band--teal { background: var(--teal); }
  .band-cut { position: absolute; left: 0; top: 0; width: 931px; height: 54px; }

  .product-bar {
    position: absolute; left: 0; top: 445px; height: 60px; width: 878px;
    display: flex; border-radius: 0 30px 30px 0; overflow: hidden;
  }
  .product {
    height: 60px; display: flex; align-items: center;
    color: var(--white-text); font-weight: 700; font-size: 27px;
  }
  .product--wallcoverings { width: 342px; background: var(--blue-1); justify-content: flex-end; padding-right: 14px; }
  .product--acoustic { width: 180px; background: var(--blue-2); padding-left: 31px; }
  .product--fabrics { width: 179px; background: var(--blue-3); padding-left: 26px; }
  .product--carpet { width: 177px; background: var(--blue-4); padding-left: 18px; }

  .company-name {
    position: absolute; left: 0; right: 0; top: 173px; text-align: center;
    font-size: 20px; font-weight: 700; color: var(--charcoal);
  }
  .person-name {
    position: absolute; left: 0; right: 0; top: 256px; text-align: center;
    font-size: 41px; font-weight: 700; color: var(--teal);
  }
  .person-mobile {
    position: absolute; left: 0; right: 0; top: 309px; text-align: center;
    font-size: 26px; color: var(--charcoal);
  }
  .contact {
    position: absolute; top: 454px; font-size: 26px; line-height: 35px; color: var(--white-text);
  }
  .contact--address { left: 44px; }
  .contact--reach { right: 27px; text-align: right; }
</style>
</head>
<body>
<div class="canvas">

  <section class="card card--front">
    <div class="wordmark">KTV</div>

    <div class="band band--grey" style="top:337px;height:54px;">
      <svg class="band-cut" viewBox="0 0 931 54" aria-hidden="true">
        <polygon points="478,0 506,0 479,27 451,27" fill="#ffffff"/>
        <polygon points="451,27 479,27 452,54 424,54" fill="#4aa593"/>
      </svg>
    </div>
    <div class="band band--teal" style="top:391px;height:171px;"></div>

    <div class="product-bar">
      <div class="product product--wallcoverings">Wallcoverings</div>
      <div class="product product--acoustic">Acoustic</div>
      <div class="product product--fabrics">Fabrics</div>
      <div class="product product--carpet">Carpet</div>
    </div>
  </section>

  <section class="card card--back">
    <div class="wordmark">KTV</div>
    <p class="company-name">Kestavel Interior Furnishings Pte Ltd</p>
    <p class="person-name">Lina Cheong</p>
    <p class="person-mobile">(65) 9172 4406</p>

    <div class="band band--teal" style="top:365px;height:54px;">
      <svg class="band-cut" viewBox="0 0 931 54" aria-hidden="true">
        <polygon points="478,0 506,0 479,27 451,27" fill="#ffffff"/>
        <polygon points="451,27 479,27 452,54 424,54" fill="#6b625d"/>
      </svg>
    </div>
    <div class="band band--grey" style="top:419px;height:142px;"></div>

    <address class="contact contact--address" style="font-style:normal;">
      47 Jalan 16 Tampines #05-02<br>
      Velmora Building Singapore 527314
    </address>
    <div class="contact contact--reach">
      (65) 6381 2257<br>
      lina@ktvfurnishings.com
    </div>
  </section>

</div>
</body>
</html>
```